Simple and Clean business card design

We would like the design to be simple clean and to incorporate our colors.

We are open to your design and talent, we have the dots in our logo as we think of it as data points and we connect data points for people.

We are open to see the great creative and clean design you bring to the table

Contact Information for Business Card

please include: name, position, email, phone and website

Font styles to use
Sans Serif

Requirements
Must have
• my colors incorporated, simplicity
Nice to have
• lots of white space, simplicity
Should not have
• complexicity/ complex art

```html
<!DOCTYPE html>
<html lang="en">
<head>
<meta charset="UTF-8">
<title>Brimly – Business Card</title>
<link rel="stylesheet" href="https://fonts.googleapis.com/css2?family=Montserrat:wght@400;500;600&display=swap">
<style>
  :root {
    --canvas: #e4e4e4;
    --card-white: #f7f7f8;
    --card-dark-top: #2e3033;
    --card-dark-bottom: #0f1011;
    --ink: #111111;
    --ink-soft: #555555;
    --brand-blue: #3b6fe0;
    --brand-green: #2e9a4a;
    --brand-yellow: #f2b50f;
    --brand-red: #de3a2c;
    --divider: #c9c9c9;
    --wordmark-light: #8d8d8f;
  }
  * { box-sizing: border-box; margin: 0; padding: 0; }
  html, body {
    width: 1200px; height: 1200px; overflow: hidden;
    background: var(--canvas);
    font-family: "Montserrat", sans-serif;
  }
  .card {
    position: absolute;
    left: 200px;
    width: 800px;
    height: 457px;
    border-radius: 24px;
    overflow: hidden;
    box-shadow: 0 14px 30px rgba(0,0,0,0.18);
  }
  .card--front { top: 110px; background: var(--card-white); }
  .card--back {
    top: 633px;
    background: linear-gradient(160deg, var(--card-dark-top) 0%, #1c1d1f 45%, var(--card-dark-bottom) 100%);
  }
  .front__band {
    position: absolute; left: 0; right: 0; bottom: 0; height: 14px;
    background: var(--brand-blue);
  }
  .wordmark {
    position: absolute;
    display: flex; align-items: center; gap: 10px;
    font-weight: 500;
    letter-spacing: 1px;
  }
  .wordmark__dot { border-radius: 50%; background: var(--brand-blue); flex: none; }
  .front__wordmark {
    left: 150px; top: 198px;
    font-size: 58px; color: var(--ink);
  }
  .front__wordmark .wordmark__dot { width: 14px; height: 14px; }
  .front__divider {
    position: absolute; left: 400px; top: 150px;
    width: 1px; height: 160px; background: var(--divider);
  }
  .details { position: absolute; left: 436px; top: 156px; }
  .details__name { font-size: 27px; font-weight: 500; color: var(--ink); line-height: 1.15; }
  .details__role { font-size: 19px; font-weight: 400; color: var(--brand-blue); line-height: 1.3; }
  .contact-list { list-style: none; margin-top: 18px; }
  .contact-list li {
    display: flex; align-items: center; gap: 9px;
    font-size: 18.5px; color: var(--ink-soft); line-height: 23px;
  }
  .contact-list svg { width: 16px; height: 16px; flex: none; }
  .back__wordmark {
    left: 0; right: 0; top: 178px; justify-content: center;
    font-size: 116px; color: var(--wordmark-light); gap: 18px;
  }
  .back__wordmark .wordmark__dot { width: 30px; height: 30px; }
</style>
</head>
<body>
  <section class="card card--front">
    <div class="wordmark front__wordmark">
      <span class="wordmark__dot"></span>
      <span class="wordmark__name">Brimly</span>
    </div>
    <div class="front__divider"></div>
    <div class="details">
      <p class="details__name">Daniel Harper</p>
      <p class="details__role">President</p>
      <ul class="contact-list">
        <li>
          <svg viewBox="0 0 16 16" aria-hidden="true"><path fill="var(--brand-green)" d="M3.6 1.5l2.2 2.6-1.3 1.9c.9 2 2.6 3.7 4.6 4.6l1.9-1.3 2.6 2.2-1.2 2.4C7 13.6 2.4 9 1.2 2.7z"/></svg>
          <span>482-306-7714</span>
        </li>
        <li>
          <svg viewBox="0 0 16 16" aria-hidden="true"><rect x="1.5" y="3.5" width="13" height="9" fill="var(--brand-yellow)"/><path d="M1.8 4l6.2 4.6L14.2 4" fill="none" stroke="#fff" stroke-width="1.2"/></svg>
          <span>hello@brimly.com</span>
        </li>
        <li>
          <svg viewBox="0 0 16 16" aria-hidden="true"><circle cx="8" cy="8" r="7" fill="var(--brand-red)"/><path d="M1.5 8h13M8 1c2 2 2 12 0 14M8 1c-2 2-2 12 0 14" fill="none" stroke="#fff" stroke-width="1"/></svg>
          <span>www.brimly.com</span>
        </li>
      </ul>
    </div>
    <div class="front__band"></div>
  </section>

  <section class="card card--back">
    <div class="wordmark back__wordmark">
      <span class="wordmark__dot"></span>
      <span class="wordmark__name">Brimly</span>
    </div>
  </section>
</body>
</html>
```